Looking for a compelling book cover, ebook and print

"Notes of a Lone Valley Bride" is a memoir in the style of "Maisie Pratt's Ledger." Watch the author interview here:
http://www.vidtornel.com/watch?v=_Q72m-9rLpX
I'm looking for a book cover for both an ebook and print edition. It should incorporate the website design, here: www.korimbradley.com (currently under construction).

I like the bright colours (esp. the orange, red, green, blue) and the various prints. I also like the worn look at the bottom and the rough edges on the white text boxes. The pencil circles around the links are a nice diary-ish thing.

Idea for the cover: the title (Notes of a Lone Valley Bride) in bold colours, looking handwritten (quickly scribbled? on a piece of scrap paper?); author name circled in pencil; possibly a "top secret" or "confidential" in red scribbled on another scrap. I'm open to other ideas too.

I like the book covers for VernOstrowicz's "Ledger" and "The Pickpocket Ledgers" by Morty Fell.

Specs:
- 1800 x 2700 pixels, 300 ppi: front cover portion of a 6" x 9" trade paperback
- 1200 x 1800 pixels, 300 ppi: print version for press releases
- 640 x 960 pixels, 72 ppi: ebook cover and product image
- 300 x 450 pixels, 72 ppi: medium-sized image for marketing email and blogs
- 100 x 150 pixels, 72 ppi: thumbnail for use in a digital signature or blog

I'm also looking for print media: bookmarks and postcard-sized flyers, perhaps posters as well. We can talk about that later.

Requirements
Must have
• professional looking! I'm going to self-publish but I don't want it to look that way!
Nice to have
• consider incorporating designs from a couple of drawings - will upload. On #1 I love pretty much everything. On #2 I especially like the smiling carrot with the planet behind him, the grinning blue apple (?) and the stars with faces.

```html
<!DOCTYPE html>
<html lang="en">
<head>
<meta charset="utf-8">
<title>Notes of a Lone Valley Bride — Cover</title>
<link rel="stylesheet" href="https://fonts.googleapis.com/css2?family=Nothing+You+Could+Do&family=Architects+Daughter&family=Stardos+Stencil:wght@700&display=swap">
<style>
  :root {
    --khaki: #d9c48e;
    --khaki-dark: #c9b073;
    --paper: #ffffff;
    --scrap: #d9a07a;
    --scrap-edge: #b97a52;
    --title-blue: #5f9fbd;
    --title-shadow: #1f2a30;
    --stamp-red: #d9262c;
    --pattern-blue: #9dc2c9;
    --pattern-cream: #efe3c2;
    --ornament-red: #e5322d;
    --ornament-orange: #f08a2a;
    --trim-teal: #6fb3b0;
    --trim-red: #d9462f;
    --pencil: #2b2b2b;
  }
  html, body {
    margin: 0;
    padding: 0;
    overflow: hidden;
    background: #ffffff;
  }
  .cover {
    position: relative;
    width: 800px;
    height: 1200px;
    overflow: hidden;
    background: var(--khaki);
  }
  .cover__art {
    position: absolute;
    inset: 0;
  }
  .cover__title {
    position: absolute;
    left: 40px;
    top: 270px;
    width: 720px;
    margin: 0;
    font-family: "Nothing You Could Do", cursive;
    font-weight: 400;
    font-size: 86px;
    line-height: 108px;
    color: var(--title-blue);
    text-align: center;
    text-shadow: 3px 4px 0 var(--title-shadow);
    transform: rotate(-2deg);
  }
  .cover__author {
    position: absolute;
    left: 110px;
    top: 835px;
    width: 560px;
    margin: 0;
    font-family: "Architects Daughter", cursive;
    font-weight: 400;
    font-size: 78px;
    color: #1c1c1c;
    text-align: center;
  }
  .stamp {
    position: absolute;
    left: 48px;
    top: 88px;
    padding: 10px 24px;
    border: 7px solid var(--stamp-red);
    border-radius: 6px;
    background: var(--paper);
    font-family: "Stardos Stencil", sans-serif;
    font-weight: 700;
    font-size: 62px;
    line-height: 1;
    color: var(--stamp-red);
    transform: rotate(-17deg);
  }
</style>
</head>
<body>
<main class="cover">
  <svg class="cover__art" width="800" height="1200" viewBox="0 0 800 1200">
    <!-- patterned top band -->
    <rect class="pattern-band" x="0" y="0" width="800" height="100" fill="var(--pattern-blue)" role="img" aria-label="Decorative blue and cream printed paper pattern"/>
    <!-- trim ribbons -->
    <rect x="0" y="128" width="800" height="6" fill="var(--trim-teal)"/>
    <rect x="0" y="136" width="800" height="4" fill="var(--trim-red)"/>
    <rect x="0" y="1148" width="800" height="4" fill="var(--trim-red)"/>
    <rect x="0" y="1154" width="800" height="6" fill="var(--trim-teal)"/>
    <rect x="0" y="1162" width="800" height="38" fill="var(--pattern-blue)" role="img" aria-label="Decorative printed paper strip"/>

    <!-- top left red ornament -->
    <path class="ornament" d="M0 0 H430 C420 70 350 120 260 110 C180 150 60 150 0 120 Z" fill="var(--ornament-red)" role="img" aria-label="Red floral paper ornament"/>
    <!-- top right orange ornament -->
    <path class="ornament" d="M520 0 H800 V560 C760 540 720 470 740 400 C700 330 640 250 660 170 C600 130 540 80 520 0 Z" fill="var(--ornament-orange)" role="img" aria-label="Orange and red paisley paper ornament"/>
    <!-- bottom right ornament -->
    <path class="ornament" d="M800 880 V1200 H560 C580 1120 640 1080 690 1060 C700 980 750 910 800 880 Z" fill="var(--ornament-red)" role="img" aria-label="Red and orange paisley paper ornament"/>

    <!-- white rough paper -->
    <path class="paper" d="M62 250 L120 236 L300 246 L520 232 L700 242 L748 262 L742 420 L752 640 L744 860 L750 1000 L720 1044 L520 1034 L300 1046 L110 1036 L58 1020 L66 820 L54 600 L64 420 Z" fill="var(--paper)"/>

    <!-- torn brown scrap behind title -->
    <path class="scrap" d="M28 262 L140 246 L360 258 L560 244 L734 266 L724 340 L738 420 L726 520 L520 534 L300 526 L96 538 L34 522 L44 440 L30 360 Z" fill="var(--scrap)" stroke="var(--scrap-edge)" stroke-width="3"/>

    <!-- pencil circle -->
    <path class="pencil-circle" d="M348 772 C560 762 700 800 700 890 C700 980 520 1000 360 996 C200 990 110 950 112 888 C114 820 240 790 400 788 C540 786 650 810 690 850" fill="none" stroke="var(--pencil)" stroke-width="2.5" stroke-linecap="round"/>
    <path d="M140 930 C200 990 420 1010 640 990" fill="none" stroke="var(--pencil)" stroke-width="1.5"/>
  </svg>

  <div class="stamp">TOP SECRET</div>
  <h1 class="cover__title">notes of a lone<br>valley bride</h1>
  <p class="cover__author">Kori Bradley</p>
</main>
</body>
</html>
```